Creation of website design for digital SAAS service for congresses, lectures and training

We are a startup in southern Germany that wants to prepare the digital bridge for all events so that the listener of a lecture or congress can digitally save the presentations and their notes. As a result, he is involved in the lecture much more intensively and will benefit from it. He can then use the app to ask the speaker / organizer to call you back using one of the picked slides. These are the leads that are generated from the events. It is a subscription model for the organizer or speakers so that he generates better results and more leads from his event. The application is running productively and can be used as a demo with a mobile phone at https://dorvane.net/demosession.html. Simply scan the QR code and pick the slides you like.
The website is a bit gruesome ..... that's why I need YOU!

The logo is Lumbo - our maksottchen, because he picks and saves the exciting slides from the presentation .....

The designer can get a free trial account for a month to get to know the app. Ends automatically!
https://app.dorvane.net/subscription/plans

Target Market(s)

Trade fair organizers, congress organizers, product management, hotel chains, associations, schools, universities, marketing organizations

Font styles to use
Sans Serif

Requirements
Must have
• The customer group are, on the one hand, marketing and sales professionals who should book the service for their customers and prospects so that more leads come from the events.
The login for the service can be done on any internet-enabled device with a browser.
Legal requirements regarding options for cookies and terms and conditions
Multilingualism DE and EN would then have to be considered technically.
The whole thing should then run on a wordpress version 5.41.
If images / photos are used, the copyright question must be clarified - what costs arise from the use and how is this to be documented if necessary.
Nice to have
• Maybe someone also creates an animation that explains the picking process nicely ... and maps the two user groups. Everyone should find themselves
Should not have
• Bad design and layout - I can top that myself!

```html
<!DOCTYPE html>
<html lang="de">
<head>
<meta charset="utf-8">
<title>dorvane – Organisation einer Kampagne oder Veranstaltung</title>
<link rel="stylesheet" href="https://fonts.googleapis.com/css2?family=Montserrat:wght@500;600;700&family=Lato:ital,wght@0,400;0,700;1,400&family=Barlow:wght@400;500;600&display=swap">
<style>
:root{
  --backdrop:#121212;
  --green:#18904f;
  --pink:#e9727a;
  --ink:#222;
  --grey-text:#9a9a9a;
  --light:#f6f6f6;
  --light-grey:#ececec;
  --dark:#262626;
  --footer-bar:#6d6d6d;
  --white:#fff;
}
*{box-sizing:border-box;margin:0;padding:0}
html,body{width:1200px;height:3046px;overflow:hidden}
body{background:var(--backdrop);font-family:"Lato",sans-serif;color:var(--ink)}
.page{position:absolute;left:45px;top:37px;width:1110px;height:2971px;background:var(--white);overflow:hidden}

/* header */
.site-header{height:95px;display:flex;align-items:center;padding-left:212px;background:var(--white)}
.brand{display:flex;align-items:center;gap:8px;font-family:"Montserrat",sans-serif;font-weight:700;font-size:24px;color:var(--green);margin-right:52px}
.brand-dot{width:30px;height:30px;border-radius:50%;background:var(--green)}
.main-nav{display:flex;align-items:center;gap:34px;font-family:"Montserrat",sans-serif;font-weight:600;font-size:11px;text-transform:uppercase}
.main-nav a{color:var(--ink);text-decoration:none}
.main-nav a.active{color:var(--pink)}
.main-nav .nav-cta{background:var(--green);color:var(--white);text-transform:none;font-size:11px;font-weight:700;padding:10px 13px}

/* hero */
.hero{position:relative;height:443px;text-align:center;color:var(--white)}
.hero-photo{position:absolute;inset:0;background:linear-gradient(180deg,#1f7a4b 0%,#2a8b57 45%,#1c7646 100%)}
.hero-content{position:relative;padding-top:150px}
.hero h1{font-family:"Montserrat",sans-serif;font-weight:700;font-size:44px;line-height:1.08}
.hero p{font-family:"Lato",sans-serif;font-size:14px;line-height:1.5;width:540px;margin:22px auto 0}
.btn-pink{display:inline-block;background:var(--pink);color:var(--white);font-family:"Montserrat",sans-serif;font-weight:700;font-size:10px;text-transform:uppercase;padding:11px 18px;text-decoration:none}
.hero .btn-pink{margin-top:20px}

/* intro */
.intro{height:244px;background:var(--light);display:flex;align-items:center;justify-content:center}
.intro p{width:650px;text-align:center;font-size:19px;line-height:1.5;color:var(--grey-text)}

/* audiences */
.audiences{display:flex;height:414px;color:var(--white);text-align:center}
.audience{flex:1;padding-top:62px}
.audience--picker{background:var(--green)}
.audience--speaker{background:var(--pink)}
.audience-visual{width:140px;height:140px;margin:0 auto;border-radius:50%}
.audience--picker .audience-visual{background:radial-gradient(circle,#f1f1ec 0%,#b9d8c6 55%,rgba(24,144,79,0) 72%)}
.audience--speaker .audience-visual{width:110px;height:120px;border-radius:6px;background:linear-gradient(180deg,rgba(255,255,255,.35),rgba(255,255,255,.12))}
.audience h2{font-family:"Barlow",sans-serif;font-weight:600;font-size:28px;margin-top:38px}
.audience--speaker h2{margin-top:48px}
.audience p{font-family:"Barlow",sans-serif;font-size:15px;line-height:1.45;width:305px;margin:12px auto 0}
.audience--speaker p{width:250px;margin-top:10px}

/* speaker feature */
.feature{display:flex;height:420px}
.feature-photo{width:487px;background:linear-gradient(120deg,#1c1e3a 0%,#2c2f52 45%,#4a3a6a 80%,#6a4a7e 100%)}
.feature-body{flex:1;background:var(--light-grey);padding:72px 60px 0 55px}
.feature h2{font-family:"Lato",sans-serif;font-weight:700;font-size:36px;line-height:1.4;color:var(--pink)}
.feature p{font-size:20px;line-height:1.5;color:var(--grey-text);margin-top:4px;width:480px}
.btn-green{display:inline-block;margin-top:42px;background:var(--green);color:var(--white);font-family:"Montserrat",sans-serif;font-weight:700;font-size:13px;text-transform:uppercase;padding:14px 30px;border-radius:22px;text-decoration:none;box-shadow:0 3px 6px rgba(0,0,0,.15)}

/* testimonials */
.testimonials{height:434px;background:var(--dark);color:var(--white);padding-top:74px}
.testimonials h2{font-family:"Montserrat",sans-serif;font-weight:600;font-size:30px;text-align:center}
.quote-grid{display:flex;gap:64px;padding-left:231px;margin-top:36px}
.quote{width:184px}
.quote p{font-style:italic;font-size:12.5px;line-height:1.5}
.quote cite{display:block;font-style:normal;font-family:"Montserrat",sans-serif;font-weight:600;font-size:11px;margin-top:20px;padding-left:4px}

/* contact */
.contact{height:580px;background:var(--light);text-align:center;padding-top:65px}
.contact h2{font-family:"Montserrat",sans-serif;font-weight:600;font-size:30px}
.contact .lead{width:780px;margin:12px auto 0;font-size:20px;line-height:1.5;color:var(--grey-text)}
.contact-form{width:564px;margin:50px auto 0;display:grid;grid-template-columns:1fr 1fr;gap:18px 18px}
.field{height:36px;background:var(--white);border:1px solid #e6e6e6;box-shadow:0 1px 3px rgba(0,0,0,.05);font-family:"Lato",sans-serif;font-size:10px;color:#aaa;text-align:left;padding:10px 12px}
.field--message{grid-column:1/3;height:104px}
.contact .btn-pink{margin-top:18px;padding:11px 22px}

/* footer */
.site-footer{height:290px;background:var(--green);color:var(--white);text-align:center;padding-top:54px;font-size:11px;line-height:1.55}
.site-footer .brand{justify-content:center;margin:0 0 20px;color:var(--white);font-size:28px}
.site-footer .brand-dot{background:var(--white)}
.footer-contact{margin-top:18px}
.social{display:flex;justify-content:center;gap:10px;margin-top:32px}
.social span{width:15px;height:15px;border-radius:50%;border:2px solid var(--white)}
.copyright{height:51px;background:var(--footer-bar);color:var(--white);font-size:10px;display:flex;align-items:center;justify-content:center}
</style>
</head>
<body>
<div class="page">

  <header class="site-header">
    <div class="brand"><span class="brand-dot"></span>dorvane</div>
    <nav class="main-nav">
      <a class="active" href="#">Abo-Varianten</a>
      <a href="#">Teilnehmer/Picker</a>
      <a href="#">Sprecher</a>
      <a href="#">Veranstalter</a>
      <a class="nav-cta" href="#">Risikofrei Testen</a>
    </nav>
  </header>

  <section class="hero">
    <div class="hero-photo" role="img" aria-label="Photo of a woman working at a laptop, tinted green"></div>
    <div class="hero-content">
      <h1>Organisation einer Kampagne<br>oder Veranstaltung</h1>
      <p>Duis aute irure dolor in reprehenderit in voluptate velit esse cillum dolore eu fugiat nulla pariatur xcepteur</p>
      <a class="btn-pink" href="#">More details</a>
    </div>
  </section>

  <section class="intro">
    <p>Lorem ipsum is a name for a common type of placeholder text. Also known as filler or dummy text, this is simply copy that serves to fill a space without actually saying anything meaningful.</p>
  </section>

  <section class="audiences">
    <div class="audience audience--picker">
      <div class="audience-visual" role="img" aria-label="Illustration of a fan of presentation slides with radiating lines"></div>
      <h2>Für die Picker</h2>
      <p>picke nur Deine wichtigen Slides erfasse Deine Notizen &nbsp;kontakte den Referenten mit Deinen Fragen</p>
    </div>
    <div class="audience audience--speaker">
      <div class="audience-visual" role="img" aria-label="Line illustration of a speaker at a lectern facing an audience"></div>
      <h2>Für die Speaker</h2>
      <p>picke nur Deine wichtigen Slides erfasse Deine Notizen &nbsp;kontakte den Referenten mit Deinen Fragen</p>
    </div>
  </section>

  <section class="feature">
    <div class="feature-photo" role="img" aria-label="Photo of a speaker in a suit holding a microphone on stage"></div>
    <div class="feature-body">
      <h2>The World’s Largest<br>Online Speaker Presentation</h2>
      <p>Lorem ipsum is a name for a common type of placeholder text. Also known as filler or dummy text, this is simply copy that serves to fill a space without actually saying anything meaningful.</p>
      <a class="btn-green" href="#">Click more details</a>
    </div>
  </section>

  <section class="testimonials">
    <h2>What our client says:</h2>
    <div class="quote-grid">
      <blockquote class="quote">
        <p>Die Präsentation in Folienwerk oder andere Applikationen einfach starten. Dann die dorvane App im Browser auf app.dorvane.net aufrufen. Nach dem Login und Start der Übertragung kann der Vortrag ganz normal ablaufen.</p>
        <cite>Sprecher</cite>
      </blockquote>
      <blockquote class="quote">
        <p>Die Zuhörer starten durch scan des QR-Code oder Eingabe des dorvane-code auf https://dorvane-code die Teilnahme an der Session. Sobald eine interessante Slide gezeigt wird, kann diese per Button gepickt werden.</p>
        <cite>- Mirela Okon</cite>
      </blockquote>
      <blockquote class="quote">
        <p>Wir bieten die Vorplanung eines Kongresses mit vielen Sessons über Vortrag Titel, Name des Sprecher,Raum,Uhrzeit etc.<br><br>Wir stellen Auswertungen über die Anzahl der</p>
        <cite>- Tobin Hartl</cite>
      </blockquote>
    </div>
  </section>

  <section class="contact">
    <h2>Sprich uns für eine Demo</h2>
    <p class="lead">Lorem ipsum is a name for a common type of placeholder text. Also known as filler or dummy text, this is simply copy that serves to</p>
    <form class="contact-form">
      <div class="field">Enter Name*</div>
      <div class="field">Enter Email*</div>
      <div class="field">Enter Subject</div>
      <div class="field">Enter Name</div>
      <div class="field field--message">Message</div>
    </form>
    <a class="btn-pink" href="#">Get a quote</a>
  </section>

  <footer class="site-footer">
    <div class="brand"><span class="brand-dot"></span>dorvane</div>
    <p>Betreiber und Kontakt:<br>Dorvane Labs GmbH<br>Lindenweg 12, 71730 Kerstal</p>
    <p class="footer-contact">Telefonnummer: 07141 555018 • E-Mail-Adresse: kontakt@dorvane.net</p>
    <div class="social" aria-label="Social media links"><span></span><span></span><span></span><span></span><span></span></div>
  </footer>
  <div class="copyright">© 2020 Dorvane Labs GmbH</div>

</div>
</body>
</html>
```